Exciting letterhead design for startup company

We need a A4 letterhead designing.

See attached file which contains the logo (on 3 different coloured backgrounds) and then the address and contact information. It also contains 4 colours that can be used.

Looking for an imaginative design. We are a young, fresh startup website design company so need a letterhead that reflects our industry.

Font styles to use
Sans Serif

```html
<!DOCTYPE html>
<html lang="en">
<head>
<meta charset="utf-8">
<title>PageNimbus Letterhead</title>
<link rel="stylesheet" href="https://fonts.googleapis.com/css2?family=Open+Sans:ital,wght@0,400;0,700;1,700&display=swap">
<style>
  :root {
    --backdrop: #e2e2e2;
    --paper: #ffffff;
    --ink: #231f20;
    --brand-blue: #0090dc;
    --brand-green: #5db95a;
    --on-blue: #ffffff;
  }
  * { box-sizing: border-box; margin: 0; padding: 0; }
  html, body {
    width: 1200px;
    height: 1200px;
    overflow: hidden;
    background: var(--backdrop);
    font-family: "Open Sans", Arial, sans-serif;
  }
  .letterhead {
    position: absolute;
    left: 211px;
    top: 50px;
    width: 778px;
    height: 1100px;
    background: var(--paper);
    overflow: hidden;
  }
  .brand-name {
    position: absolute;
    left: 79px;
    top: 64px;
    font-weight: 700;
    font-size: 40px;
    line-height: 48px;
    letter-spacing: -1.2px;
    color: var(--ink);
  }
  .footer-band {
    position: absolute;
    left: 0;
    bottom: 0;
    width: 778px;
    height: 150px;
    background: linear-gradient(90deg, var(--brand-green) 0%, var(--brand-blue) 45%, var(--brand-blue) 100%);
  }
  .footer-details {
    position: absolute;
    right: 28px;
    top: 1000px;
    text-align: right;
    color: var(--on-blue);
  }
  .company-title {
    font-weight: 700;
    font-style: italic;
    font-size: 21px;
    line-height: 26px;
    letter-spacing: 0.2px;
  }
  .company-address {
    font-size: 10.5px;
    line-height: 14px;
    margin-top: 4px;
  }
  .company-contact {
    display: flex;
    justify-content: flex-end;
    align-items: center;
    gap: 6px;
    font-size: 12px;
    line-height: 16px;
    margin-top: 6px;
  }
  .contact-icon { width: 13px; height: 11px; fill: var(--on-blue); }
</style>
</head>
<body>
  <main class="letterhead">
    <div class="brand-name">PageNimbus</div>

    <div class="footer-band" role="img" aria-label="Decorative footer band in the brand's green and blue tones"></div>

    <div class="footer-details">
      <p class="company-title">PageNimbus Limited</p>
      <p class="company-address">Unit 4, Larkspur Court, Leeds LS2 7QD.<br>Registered in England &amp; Wales | Company No 04172638</p>
      <p class="company-contact">
        <span>hello@pagenimbus.co.uk</span>
        <svg class="contact-icon" viewBox="0 0 13 11" aria-label="email"><path d="M0 1h13v9H0z M1 2v.4l5.5 4 5.5-4V2z" fill-rule="evenodd"/></svg>
        <span>0845 210 3378</span>
        <svg class="contact-icon" viewBox="0 0 13 11" aria-label="phone"><path d="M1 3 C1 1 3 0.5 6.5 0.5 S12 1 12 3 L9.5 3.6 L9 2.4 C7.5 2 5.5 2 4 2.4 L3.5 3.6 Z M3 5 L4.5 3.5 H8.5 L10 5 L11 10 H2 Z"/></svg>
      </p>
    </div>
  </main>
</body>
</html>
```